Brightpath Letterhead

We would like a letterhead for our company. I have uploaded our logo.

Brightpath Ridge Consulting
1450 W Corliss Ave Ste 310
Cedar Hollow, TX 76142
833-517-2906

```html
<!DOCTYPE html>
<html lang="en">
<head>
<meta charset="utf-8">
<title>Brightpath Ridge Consulting Letterhead</title>
<link href="https://fonts.googleapis.com/css2?family=Josefin+Sans:wght@600&family=Didact+Gothic&display=swap" rel="stylesheet">
<style>
  :root {
    --teal: #0b5d6b;
    --mint: #6cc49a;
    --paper: #ffffff;
    --backdrop: #ececec;
  }
  html, body {
    margin: 0;
    padding: 0;
    width: 1200px;
    height: 1200px;
    overflow: hidden;
    background: var(--backdrop);
  }
  .letterhead {
    position: absolute;
    left: 172px;
    top: 50px;
    width: 855px;
    height: 1100px;
    background: var(--paper);
    overflow: hidden;
  }
  .brand {
    position: absolute;
    left: 60px;
    top: 56px;
    display: flex;
    align-items: center;
    gap: 14px;
  }
  .brand-dot {
    width: 60px;
    height: 60px;
    border-radius: 50%;
    background: var(--teal);
    flex: none;
  }
  .brand-name {
    font-family: "Josefin Sans", sans-serif;
    font-weight: 600;
    color: var(--teal);
    font-size: 31px;
    line-height: 36px;
    letter-spacing: 3px;
    text-transform: uppercase;
    margin: 0;
    padding-top: 6px;
    white-space: nowrap;
  }
  .contact {
    position: absolute;
    left: 567px;
    top: 59px;
    height: 58px;
    border-left: 2px solid var(--teal);
    padding-left: 14px;
    font-family: "Didact Gothic", sans-serif;
    font-size: 17.5px;
    color: var(--teal);
    line-height: 23px;
    font-style: normal;
    margin-top: -4px;
  }
  .contact-line {
    display: flex;
    align-items: center;
    gap: 6px;
    margin: 0;
    white-space: nowrap;
  }
  .contact-line.indent { padding-left: 21px; }
  .contact-icon { width: 15px; height: 15px; flex: none; }
  .footer-band {
    position: absolute;
    left: 0;
    bottom: 0;
    width: 855px;
    height: 29px;
  }
</style>
</head>
<body>
  <main class="letterhead">
    <header>
      <div class="brand">
        <span class="brand-dot"></span>
        <h1 class="brand-name">Brightpath Ridge<br>Consulting</h1>
      </div>
      <address class="contact">
        <p class="contact-line">
          <svg class="contact-icon" viewBox="0 0 16 16" aria-hidden="true">
            <path d="M8 1a5 5 0 0 0-5 5c0 3.8 5 9 5 9s5-5.2 5-9a5 5 0 0 0-5-5zm0 7a2 2 0 1 1 0-4 2 2 0 0 1 0 4z" fill="var(--mint)"/>
          </svg>
          1450 W Corliss Ave Ste 310
        </p>
        <p class="contact-line indent">Cedar Hollow, TX 76142</p>
        <p class="contact-line">
          <svg class="contact-icon" viewBox="0 0 16 16" aria-hidden="true">
            <path d="M4 2l2 3-1.3 1.3c.8 1.8 2.2 3.2 4 4L10 9l3 2-1.2 2.3C7 13 3 9 2.7 3.2z" fill="none" stroke="var(--mint)" stroke-width="1.4" stroke-linejoin="round"/>
            <path d="M9.5 2.5a4 4 0 0 1 4 4M9.5 5a1.6 1.6 0 0 1 1.6 1.6" fill="none" stroke="var(--mint)" stroke-width="1.2" stroke-linecap="round"/>
          </svg>
          833-517-2906
        </p>
      </address>
    </header>
    <svg class="footer-band" viewBox="0 0 855 29" preserveAspectRatio="none" aria-hidden="true">
      <polygon points="0,0 431,0 408,29 0,29" fill="var(--mint)"/>
      <polygon points="443,0 855,0 855,29 419,29" fill="var(--teal)"/>
    </svg>
  </main>
</body>
</html>
```